Ridge 9 Ridge Turbine Rentals Pty Ltd

We are a hire company based on the Gold Coast in Australia, we Hire out Generators to construction sites, music festivals, parties, fetes etc. Anywhere where power is required we can provide it.

Ridge 9 Ridge Turbine Rentals pty Ltd also provides all leads, distribution boards, Qualified Electricians to perform all connections. we offer refuelling services and mechanical services. 24Hr on call service - to an actual english speaking operator.

Slogan ''Power Anywhere Anytime"

Industry/Entity Type

Construction

Contact Information for Business Card

M: 0417285963
E: bookings@ridge9ridgeturbinerentals.com.au

```html
<!DOCTYPE html>
<html lang="en">
<head>
<meta charset="utf-8">
<title>Ridge 9 Ridge Turbine Rentals – Business Card</title>
<link rel="stylesheet" href="https://fonts.googleapis.com/css2?family=Open+Sans:wght@400;600;800&display=swap">
<style>
  :root {
    --page: #2b2b2d;
    --card-dark: #000000;
    --card-light: #ffffff;
    --ink: #111111;
    --ink-soft: #2a2a2a;
    --accent: #2f7fb0;
    --accent-light: #6fb3d6;
    --on-dark: #ffffff;
  }
  * { margin: 0; padding: 0; box-sizing: border-box; }
  html, body {
    width: 1200px; height: 900px; overflow: hidden;
    background: var(--page);
    font-family: "Open Sans", Arial, sans-serif;
  }
  .canvas {
    position: relative; width: 1200px; height: 900px;
  }
  .card {
    position: absolute; left: 280px; width: 640px; height: 366px;
    border-radius: 26px; overflow: hidden;
  }
  .card--front { top: 60px; background: var(--card-dark); }
  .card--back { top: 474px; background: var(--card-light); }

  /* front */
  .front-brand {
    position: absolute; left: 150px; top: 110px;
    display: flex; align-items: center; gap: 18px;
  }
  .brand-dot {
    width: 72px; height: 72px; border-radius: 50%;
    background: linear-gradient(135deg, var(--accent-light), var(--accent));
    flex: none;
  }
  .brand-name {
    font-weight: 800; text-transform: uppercase; line-height: 1.05;
  }
  .front-brand .brand-name { color: var(--on-dark); font-size: 30px; }
  .slogan {
    position: absolute; left: 0; right: 0; bottom: 40px;
    text-align: center; color: var(--on-dark);
    font-size: 16px; letter-spacing: 1.5px; font-weight: 400;
  }

  /* back */
  .back-brand {
    position: absolute; left: 40px; top: 150px;
    display: flex; align-items: center; gap: 10px;
  }
  .back-brand .brand-dot { width: 48px; height: 48px; }
  .back-brand .brand-name { color: var(--ink); font-size: 16px; }
  .divider {
    position: absolute; left: 252px; top: 120px; width: 2px; height: 140px;
    background: var(--accent);
  }
  .contact {
    position: absolute; left: 268px; top: 120px;
  }
  .person-name {
    font-weight: 800; font-size: 28px; color: var(--ink); line-height: 1.1;
    text-transform: uppercase;
  }
  .person-role {
    font-size: 15px; color: var(--accent); text-transform: uppercase;
    letter-spacing: 0.5px; margin-bottom: 10px;
  }
  .contact-line {
    display: flex; align-items: center; gap: 8px;
    font-size: 15px; color: var(--ink-soft); line-height: 1.5;
  }
  .contact-line svg { width: 14px; height: 14px; flex: none; }
</style>
</head>
<body>
<main class="canvas">
  <section class="card card--front" aria-label="Card front">
    <div class="front-brand">
      <span class="brand-dot" aria-hidden="true"></span>
      <span class="brand-name">Ridge 9 Ridge<br>Turbine Rentals</span>
    </div>
    <p class="slogan">POWER ANYWHERE ANYTIME</p>
  </section>

  <section class="card card--back" aria-label="Card back">
    <div class="back-brand">
      <span class="brand-dot" aria-hidden="true"></span>
      <span class="brand-name">Ridge 9 Ridge<br>Turbine Rentals</span>
    </div>
    <span class="divider" aria-hidden="true"></span>
    <div class="contact">
      <p class="person-name">Jake Holloway</p>
      <p class="person-role">Director</p>
      <p class="contact-line">
        <svg viewBox="0 0 14 14" aria-hidden="true"><rect x="3.5" y="1" width="7" height="12" rx="1.3" fill="none" stroke="#2a2a2a" stroke-width="1.4"/><circle cx="7" cy="10.8" r="0.8" fill="#2a2a2a"/></svg>
        0417285963
      </p>
      <p class="contact-line">
        <svg viewBox="0 0 14 14" aria-hidden="true"><rect x="1" y="3" width="12" height="8.5" rx="1" fill="none" stroke="#2f7fb0" stroke-width="1.4"/><path d="M1.5 3.5 L7 8 L12.5 3.5" fill="none" stroke="#2f7fb0" stroke-width="1.4"/></svg>
        bookings@ridge9ridgeturbinerentals.com.au
      </p>
    </div>
  </section>
</main>
</body>
</html>
```